Brightwave Business Card

Professional Business Card Design required using the attached contact information.

Contact information can be rearranged as required.

The company is a new start up venture developing solar systems, the branding should be in keeping with that of one of the investors whose website is as follows https://www.quorvex.com/

```html
<!DOCTYPE html>
<html lang="en">
<head>
<meta charset="utf-8">
<title>Brightwave Renewables – Business Card</title>
<link rel="stylesheet" href="https://fonts.googleapis.com/css2?family=Montserrat:wght@600&family=Roboto:wght@300;400;700&display=swap">
<style>
  :root {
    --backdrop: #5a5a5a;
    --card: #232323;
    --edge: #1f6b55;
    --accent: #2d6b55;
    --logo-light: #f4f4f4;
    --logo-dark: #2e2e2e;
    --text: #e6e6e6;
    --divider: #6a6a6a;
  }
  * { box-sizing: border-box; margin: 0; padding: 0; }
  html, body { width: 1200px; height: 1124px; overflow: hidden; }
  body {
    background: var(--backdrop);
    display: flex;
    flex-direction: column;
    align-items: center;
    justify-content: center;
    gap: 36px;
    font-family: "Roboto", sans-serif;
  }
  .card {
    width: 880px;
    height: 502px;
    background: var(--card);
    border-bottom: 4px solid var(--edge);
    border-left: 4px solid var(--edge);
    position: relative;
    box-shadow: 0 10px 24px rgba(0,0,0,0.35);
  }
  .wordmark {
    font-family: "Montserrat", sans-serif;
    font-weight: 600;
    letter-spacing: 0.08em;
    text-transform: uppercase;
    white-space: nowrap;
    display: flex;
    align-items: center;
    gap: 18px;
  }
  .wordmark-dot { width: 12px; height: 12px; border-radius: 50%; background: var(--accent); }

  /* back side */
  .card-back .wordmark {
    position: absolute; left: 50%; top: 200px; transform: translateX(-50%);
    font-size: 44px; color: var(--logo-dark);
  }
  .card-back .site {
    position: absolute; right: 150px; top: 330px;
    font-size: 20px; font-weight: 300; color: var(--text);
  }

  /* front side */
  .card-front .wordmark {
    position: absolute; left: 50%; top: 90px; transform: translateX(-50%);
    font-size: 44px; color: var(--logo-light);
  }
  .contact-row {
    position: absolute; left: 0; right: 0; top: 240px;
    display: flex; justify-content: center; align-items: center; gap: 34px;
  }
  .person-name {
    font-weight: 700; font-size: 32px; color: var(--accent); letter-spacing: 0.01em;
  }
  .divider { width: 1px; height: 96px; background: var(--divider); }
  .contact-list { list-style: none; display: flex; flex-direction: column; gap: 4px; }
  .contact-list li {
    display: flex; align-items: center; gap: 12px;
    font-size: 20px; font-weight: 300; color: var(--text);
  }
  .contact-list svg { width: 16px; height: 16px; flex: none; }
  .address {
    position: absolute; left: 0; right: 0; top: 395px; text-align: center;
    font-size: 21px; font-weight: 300; color: var(--text);
  }
</style>
</head>
<body>
  <section class="card card-back">
    <div class="wordmark"><span>Brightwave</span><span class="wordmark-dot"></span><span>Renewables</span></div>
    <p class="site">www.quorvex.com</p>
  </section>

  <section class="card card-front">
    <div class="wordmark"><span>Brightwave</span><span class="wordmark-dot"></span><span>Renewables</span></div>
    <div class="contact-row">
      <h1 class="person-name">DANIEL MARSH</h1>
      <span class="divider"></span>
      <ul class="contact-list">
        <li>
          <svg viewBox="0 0 16 16" aria-hidden="true"><path d="M3 1.5l2.5 0 1 3.5-1.6 1.2a8 8 0 0 0 4.9 4.9L11 9.5l3.5 1v2.5c0 .8-.7 1.5-1.5 1.5C7 14.5 1.5 9 1.5 3c0-.8.7-1.5 1.5-1.5z" fill="#2d6b55"/></svg>
          +1 (555) 014-2290
        </li>
        <li>
          <svg viewBox="0 0 16 16" aria-hidden="true"><rect x="1.5" y="3.5" width="13" height="9" fill="none" stroke="#2d6b55" stroke-width="1.4"/><path d="M1.5 3.5L8 9l6.5-5.5" fill="none" stroke="#2d6b55" stroke-width="1.4"/></svg>
          daniel.marsh@brightwave-renewables.com
        </li>
        <li>
          <svg viewBox="0 0 16 16" aria-hidden="true"><circle cx="8" cy="8" r="6.5" fill="none" stroke="#2d6b55" stroke-width="1.4"/><ellipse cx="8" cy="8" rx="2.8" ry="6.5" fill="none" stroke="#2d6b55" stroke-width="1.2"/><path d="M1.5 8h13" stroke="#2d6b55" stroke-width="1.2"/></svg>
          www.quorvex.com
        </li>
      </ul>
    </div>
    <p class="address">120 Harbor Street, Boston, MA 02110</p>
  </section>
</body>
</html>
```